GRAPHIC DESIGN FOR RESTAURANT MENU FOR HEALTHY RESTAURANT

I am looking for a graphic design for our menu displayed on a TV screen. Please ensure the file will fit on a TV screen nicely. We are looking for a clean design , with the following items. We would also like to include a couple of photos.
Breakfast:
Protein Chocolate Chip Pancakes - $12.95
Dawn Hustle Burrito- $11.95
Hearty Harvest Omelette - $12.95
Lunch
Butter Chicken - $13.95
Chicken Quesadilla - $13.45
Coconut Garlic Shrimp - $15.95
Goat Cheese Stuffed Chicken - $14.95
Chipotle Steak Wrap - $12.95
Turkey Meatball Fettuccini - $13.45
Chicken Alfredo - $13.45
Chicken Parmesan - $13.95
Pesto Chicken Pasta - $13.45
Steak Bite and Green Stir Fry - $13.45
Asian Chicken Teriyaki - $13.45
Please include our logo

```html
<!DOCTYPE html>
<html lang="en">
<head>
<meta charset="utf-8">
<title>Verdant Healthy Kitchen Menu</title>
<link href="https://fonts.googleapis.com/css2?family=Fira+Sans+Condensed:wght@500&family=Montserrat:wght@400;500;600;700;800&display=swap" rel="stylesheet">
<style>
  :root {
    --cream: #f3f2a6;
    --leaf: #9bbd3a;
    --leaf-dark: #7aa024;
    --ink: #222222;
    --muted: #555555;
    --white: #ffffff;
  }
  * { margin: 0; padding: 0; box-sizing: border-box; }
  html, body { width: 857px; height: 1200px; overflow: hidden; background: var(--cream); }
  .menu-board {
    position: relative; width: 857px; height: 1200px; overflow: hidden;
    font-family: 'Montserrat', sans-serif; background: var(--cream);
  }
  .backdrop { position: absolute; inset: 0; }
  .brand { position: absolute; left: 80px; top: 282px; }
  .brand-name {
    font-size: 64px; font-weight: 700; color: var(--leaf-dark); letter-spacing: 1px; line-height: 1;
    display: flex; align-items: center; gap: 10px;
  }
  .brand-dot { width: 16px; height: 16px; border-radius: 50%; background: var(--leaf-dark); }
  .brand-tagline { margin-top: 8px; font-size: 19px; font-weight: 700; color: var(--leaf); white-space: nowrap; }
  .menu-title { position: absolute; left: 132px; top: 388px; font-size: 58px; font-weight: 800; color: var(--ink); letter-spacing: 1px; }
  .section-title {
    position: absolute; font-size: 27px; font-weight: 700; color: var(--ink);
    display: flex; align-items: center; gap: 14px;
  }
  .section-title::before { content: ""; width: 9px; height: 9px; border-radius: 50%; background: var(--ink); }
  .dish { position: absolute; width: 292px; }
  .dish-head {
    display: flex; justify-content: space-between; align-items: baseline; gap: 10px;
    font-size: 19px; font-weight: 600; color: var(--leaf); white-space: nowrap;
  }
  .dish-head.tight { font-family: 'Fira Sans Condensed', sans-serif; font-weight: 500; font-size: 19px; }
  .dish-head.stacked { display: block; white-space: normal; line-height: 26px; }
  .dish-head.stacked .price { float: right; }
  .dish-desc { margin-top: 6px; font-size: 10.5px; line-height: 14px; color: var(--muted); }
  .delivery {
    position: absolute; left: 15px; top: 1076px; width: 268px; height: 70px;
    background: var(--leaf); border-radius: 0 8px 8px 0; padding: 6px 0 0 52px;
  }
  .delivery .section-title { position: static; margin-left: -24px; }
  .delivery-phone {
    display: flex; align-items: center; gap: 8px; margin-top: 2px;
    font-size: 16px; font-weight: 600; color: var(--white);
  }
</style>
</head>
<body>
<main class="menu-board">
  <svg class="backdrop" width="857" height="1200" viewBox="0 0 857 1200">
    <defs>
      <linearGradient id="pasta" x1="0" y1="0" x2="1" y2="1">
        <stop offset="0" stop-color="#dfe3e6"/><stop offset="0.5" stop-color="#c2452a"/><stop offset="1" stop-color="#e9ecee"/>
      </linearGradient>
      <linearGradient id="wrap" x1="0" y1="0" x2="1" y2="1">
        <stop offset="0" stop-color="#e6e9ec"/><stop offset="0.5" stop-color="#b58a5c"/><stop offset="1" stop-color="#d9c4a4"/>
      </linearGradient>
      <linearGradient id="omelette" x1="0" y1="0" x2="1" y2="1">
        <stop offset="0" stop-color="#dfe3e6"/><stop offset="0.45" stop-color="#8a5a32"/><stop offset="0.7" stop-color="#e9c25a"/><stop offset="1" stop-color="#eef0f2"/>
      </linearGradient>
      <linearGradient id="orb" x1="0" y1="0" x2="1" y2="1">
        <stop offset="0" stop-color="#c9dc6a"/><stop offset="1" stop-color="#8fb335"/>
      </linearGradient>
    </defs>
    <rect width="857" height="1200" fill="var(--cream)"/>
    <path d="M0 0 H857 V405 C770 395 690 360 600 300 C520 250 470 215 380 212 C250 210 120 250 10 330 L0 330 Z" fill="var(--leaf)"/>
    <path d="M0 250 C120 215 250 205 360 225 C450 245 500 300 560 340 C620 380 700 410 857 420 V1200 H0 Z" fill="var(--cream)"/>
    <g role="img" aria-label="Photo of fettuccine with meatballs in tomato sauce">
      <ellipse cx="185" cy="95" rx="205" ry="145" fill="url(#pasta)" stroke="var(--white)" stroke-width="10"/>
    </g>
    <g role="img" aria-label="Photo of a halved breakfast burrito on parchment">
      <circle cx="705" cy="150" r="205" fill="url(#wrap)" stroke="var(--white)" stroke-width="10"/>
    </g>
    <path d="M420 1200 C450 1030 580 955 700 950 C780 948 830 965 857 985 V1200 Z" fill="var(--leaf)"/>
    <g role="img" aria-label="Photo of an omelette with wholegrain toast">
      <path d="M470 1200 C480 1070 590 985 705 980 C780 978 830 995 857 1010 V1200 Z" fill="url(#omelette)" stroke="var(--white)" stroke-width="10"/>
    </g>
    <circle cx="0" cy="600" r="82" fill="url(#orb)"/>
    <circle cx="843" cy="910" r="55" fill="url(#orb)"/>
    <circle cx="325" cy="1218" r="42" fill="url(#orb)" opacity="0.8"/>
  </svg>

  <header class="brand">
    <div class="brand-name"><span class="brand-dot"></span>VERDANT</div>
    <div class="brand-tagline">HEALTHY KITCHEN &nbsp;|&nbsp; MEAL PREP</div>
  </header>

  <h1 class="menu-title">MENU</h1>

  <h2 class="section-title" style="left:65px; top:460px;">LUNCH</h2>

  <article class="dish" style="left:91px; top:512px;">
    <div class="dish-head"><span>Butter Chicken</span><span class="price">$13.95</span></div>
    <p class="dish-desc">Lorem Ipsum is simply dummy text of the printing and typesetting industry.</p>
  </article>
  <article class="dish" style="left:91px; top:581px;">
    <div class="dish-head"><span>Chicken Quesadilla</span><span class="price">$13.45</span></div>
    <p class="dish-desc">Lorem Ipsum is simply dummy text of the printing and typesetting industry.</p>
  </article>
  <article class="dish" style="left:91px; top:651px;">
    <div class="dish-head"><span>Coconut Garlic Shrimp</span><span class="price">$15.95</span></div>
    <p class="dish-desc">Lorem Ipsum is simply dummy text of the printing and typesetting industry.</p>
  </article>
  <article class="dish" style="left:91px; top:721px;">
    <div class="dish-head tight"><span>Goat Cheese Stuffed Chicken</span><span class="price">$14.95</span></div>
    <p class="dish-desc">Lorem Ipsum is simply dummy text of the printing and typesetting industry.</p>
  </article>
  <article class="dish" style="left:91px; top:790px;">
    <div class="dish-head tight"><span>Turkey Meatball Fettuccini</span><span class="price">$13.45</span></div>
    <p class="dish-desc">Lorem Ipsum is simply dummy text of the printing and typesetting industry.</p>
  </article>
  <article class="dish" style="left:91px; top:859px;">
    <div class="dish-head"><span>Chicken Alfredo</span><span class="price">$13.45</span></div>
    <p class="dish-desc">Lorem Ipsum is simply dummy text of the printing and typesetting industry.</p>
  </article>
  <article class="dish" style="left:91px; top:928px;">
    <div class="dish-head"><span>Chicken Parmesan</span><span class="price">$13.95</span></div>
    <p class="dish-desc">Lorem Ipsum is simply dummy text of the printing and typesetting industry.</p>
  </article>
  <article class="dish" style="left:91px; top:997px;">
    <div class="dish-head"><span>Pesto Chicken Pasta</span><span class="price">$13.45</span></div>
    <p class="dish-desc">Lorem Ipsum is simply dummy text of the printing and typesetting industry.</p>
  </article>

  <article class="dish" style="left:485px; top:510px;">
    <div class="dish-head tight"><span>Steak Bite and Green Stir Fry</span><span class="price">$13.45</span></div>
    <p class="dish-desc">Lorem Ipsum is simply dummy text of the printing and typesetting industry.</p>
  </article>
  <article class="dish" style="left:485px; top:576px;">
    <div class="dish-head"><span>Asian Chicken Teriyaki</span><span class="price">$13.45</span></div>
    <p class="dish-desc">Lorem Ipsum is simply dummy text of the printing and typesetting industry.</p>
  </article>
  <article class="dish" style="left:485px; top:642px;">
    <div class="dish-head"><span>Chipotle Steak Wrap</span><span class="price">$12.95</span></div>
    <p class="dish-desc">Lorem Ipsum is simply dummy text of the printing and typesetting industry.</p>
  </article>

  <h2 class="section-title" style="left:462px; top:704px;">BREAKFAST</h2>

  <article class="dish" style="left:485px; top:748px;">
    <div class="dish-head stacked">Protein Chocolate Chip<br>Pancakes<span class="price">$12.95</span></div>
    <p class="dish-desc" style="margin-top:2px;">Lorem Ipsum is simply dummy text of the printing and typesetting industry.</p>
  </article>
  <article class="dish" style="left:485px; top:838px;">
    <div class="dish-head"><span>Dawn Hustle Burrito</span><span class="price">$11.95</span></div>
    <p class="dish-desc">Lorem Ipsum is simply dummy text of the printing and typesetting industry.</p>
  </article>
  <article class="dish" style="left:485px; top:902px;">
    <div class="dish-head tight"><span>Hearty Harvest Omelette</span><span class="price">$12.95</span></div>
    <p class="dish-desc">Lorem Ipsum is simply dummy text of the printing and typesetting industry.</p>
  </article>

  <aside class="delivery">
    <h2 class="section-title">DELIVERY</h2>
    <div class="delivery-phone">
      <svg width="20" height="20" viewBox="0 0 20 20" aria-hidden="true">
        <circle cx="10" cy="10" r="10" fill="var(--white)"/>
        <path d="M7 5 L8.6 7.6 L7.6 8.8 C8.3 10.4 9.6 11.7 11.2 12.4 L12.4 11.4 L15 13 L14 15 C9.5 15 5 10.5 5 6 Z" fill="var(--leaf)"/>
      </svg>
      <span>+0 555 010 274</span>
    </div>
  </aside>
</main>
</body>
</html>
```